Timber Ridge Land Services Business Cards

Need to create a business card with the company logo "Timber Ridge Land Services". The business will provide forestry mulching for land clearing and vegetation control, brush and small tree removal, wildlife habitat improvement and trail and property access creation.

```html
<!DOCTYPE html>
<html lang="en">
<head>
<meta charset="utf-8">
<title>Timber Ridge Land Services – Business Cards</title>
<link href="https://fonts.googleapis.com/css2?family=Lato:wght@400;700;900&display=swap" rel="stylesheet">
<style>
  :root {
    --bg: #c9c9c9;
    --forest: #005a48;
    --forest-text: #0b5c49;
    --leaf: #4caf50;
    --ink: #1c1c1c;
    --white: #ffffff;
  }
  * { margin: 0; padding: 0; box-sizing: border-box; }
  html, body { width: 1200px; height: 802px; overflow: hidden; }
  body {
    background: var(--bg);
    font-family: "Lato", sans-serif;
    position: relative;
  }
  .card {
    position: absolute;
    width: 530px;
    height: 304px;
    border-radius: 22px;
    box-shadow: 0 10px 26px rgba(0,0,0,0.28);
    overflow: hidden;
  }
  /* Front card */
  .card--front { left: 40px; top: 249px; background: var(--white); }
  .brand {
    position: absolute;
    left: 30px; top: 0; width: 220px; height: 100%;
    display: flex; flex-direction: column; justify-content: center; align-items: center;
    color: var(--forest-text);
    font-weight: 900;
    text-transform: uppercase;
    text-align: center;
  }
  .brand__square { width: 26px; height: 26px; background: var(--leaf); margin-bottom: 14px; }
  .brand__name { font-size: 30px; line-height: 1; letter-spacing: 1px; }
  .brand__sub { font-size: 15px; letter-spacing: 2.5px; margin-top: 6px; }
  .divider {
    position: absolute; left: 270px; top: 52px; width: 1px; height: 200px;
    background: var(--forest-text);
  }
  .contact { position: absolute; left: 292px; top: 52px; color: var(--ink); }
  .contact__name {
    font-size: 21px; font-weight: 700; color: var(--forest-text);
    text-transform: uppercase; letter-spacing: 0.5px;
  }
  .contact__role { font-size: 13px; margin-top: 2px; }
  .contact__list { list-style: none; margin-top: 22px; font-size: 12.5px; line-height: 1.45; }
  .contact__item { display: flex; align-items: flex-start; gap: 9px; margin-bottom: 5px; }
  .contact__icon { width: 14px; height: 14px; flex: none; margin-top: 2px; }
  /* Back card */
  .card--back {
    left: 630px; top: 249px; background: var(--forest); color: var(--white);
    display: flex; flex-direction: column; align-items: center; text-align: center;
  }
  .card--back .brand {
    position: static; width: auto; height: auto; color: var(--white); margin-top: 48px;
  }
  .card--back .brand__square { background: var(--white); }
  .card--back .brand__name { font-size: 40px; }
  .card--back .brand__sub { font-size: 19px; letter-spacing: 3.5px; }
  .services {
    margin-top: 30px; padding: 0 34px; font-size: 15px; line-height: 1.4;
  }
</style>
</head>
<body>
  <section class="card card--front" aria-label="Business card front">
    <div class="brand">
      <span class="brand__square"></span>
      <span class="brand__name">Timber Ridge</span>
      <span class="brand__sub">Land Services</span>
    </div>
    <div class="divider"></div>
    <div class="contact">
      <p class="contact__name">Daniel Harper</p>
      <p class="contact__role">Managing Director</p>
      <ul class="contact__list">
        <li class="contact__item">
          <svg class="contact__icon" viewBox="0 0 24 24"><path fill="#0b5c49" d="M6.6 10.8a15.1 15.1 0 0 0 6.6 6.6l2.2-2.2a1 1 0 0 1 1-.25 11.4 11.4 0 0 0 3.6.57 1 1 0 0 1 1 1V20a1 1 0 0 1-1 1A17 17 0 0 1 3 4a1 1 0 0 1 1-1h3.5a1 1 0 0 1 1 1c0 1.25.2 2.45.57 3.6a1 1 0 0 1-.25 1z"/></svg>
          <span>044-555 018 274</span>
        </li>
        <li class="contact__item">
          <svg class="contact__icon" viewBox="0 0 24 24"><rect x="2" y="5" width="20" height="14" rx="2" fill="#0b5c49"/><path d="M3 6l9 7 9-7" stroke="#fff" stroke-width="2" fill="none"/></svg>
          <span>info@timberridgeland.com<br>www.timberridgeland.com</span>
        </li>
        <li class="contact__item">
          <svg class="contact__icon" viewBox="0 0 24 24"><circle cx="12" cy="12" r="10" fill="#0b5c49"/><path d="M2 12h20M12 2c3 3 3 17 0 20M12 2c-3 3-3 17 0 20" stroke="#fff" stroke-width="1.5" fill="none"/></svg>
          <span>18 Cedar Hollow Road<br>40512, Oakfield</span>
        </li>
      </ul>
    </div>
  </section>

  <section class="card card--back" aria-label="Business card back">
    <div class="brand">
      <span class="brand__square"></span>
      <span class="brand__name">Timber Ridge</span>
      <span class="brand__sub">Land Services</span>
    </div>
    <p class="services">Forestry mulching for land clearing and vegetation control • Brush and small tree removal • Wildlife habitat improvement and Trail and property access creation</p>
  </section>
</body>
</html>
```